Business Card Design for Engineering Firm

Need a business card design for small mechanical and plumbing engineering form based in Utah. Design should be customizable for all employees.

```html
<!DOCTYPE html>
<html lang="en">
<head>
<meta charset="utf-8">
<title>Marlowe Engineering – Business Card</title>
<link rel="stylesheet" href="https://fonts.googleapis.com/css2?family=Montserrat:wght@500&family=Lato:wght@400;700&display=swap">
<style>
  :root {
    --brand-red: #7d0000;
    --charcoal: #3f3f41;
    --text-gray: #5a5a5c;
    --card-white: #ffffff;
    --stage: #e4e4e6;
  }
  * { box-sizing: border-box; margin: 0; padding: 0; }
  html, body { width: 1200px; height: 952px; overflow: hidden; }
  body {
    background: var(--stage);
    font-family: "Lato", sans-serif;
    position: relative;
  }
  .card {
    position: absolute;
    top: 326px;
    width: 525px;
    height: 300px;
    background: var(--card-white);
    border-radius: 24px;
    overflow: hidden;
    box-shadow: 0 6px 18px rgba(0,0,0,0.18);
  }
  .card-front { left: 50px; }
  .card-back { left: 625px; }

  /* Brand lockup */
  .lockup {
    position: absolute;
    display: flex;
    align-items: center;
  }
  .lockup-mark {
    background: var(--brand-red);
    flex: none;
  }
  .lockup-divider {
    width: 1px;
    background: var(--text-gray);
    opacity: 0.6;
  }
  .lockup-name {
    font-family: "Montserrat", sans-serif;
    font-weight: 500;
    color: var(--brand-red);
    line-height: 1;
  }
  .lockup-sub {
    font-family: "Montserrat", sans-serif;
    font-weight: 500;
    color: var(--text-gray);
    text-transform: uppercase;
  }

  .card-front .lockup { top: 46px; left: 150px; gap: 16px; }
  .card-front .lockup-mark { width: 44px; height: 44px; }
  .card-front .lockup-divider { height: 64px; }
  .card-front .lockup-name { font-size: 32px; letter-spacing: 0.5px; }
  .card-front .lockup-sub { font-size: 10px; letter-spacing: 7.6px; margin-top: 6px; }

  /* Person */
  .person {
    position: absolute;
    top: 150px;
    left: 34px;
  }
  .person-name {
    font-weight: 700;
    font-size: 17px;
    color: var(--brand-red);
    letter-spacing: 0.3px;
  }
  .person-title {
    font-size: 13px;
    color: var(--text-gray);
    margin-top: 4px;
  }

  /* Contacts */
  .contacts {
    position: absolute;
    top: 134px;
    left: 270px;
    list-style: none;
    display: flex;
    flex-direction: column;
    gap: 9px;
  }
  .contact-item {
    display: flex;
    align-items: center;
    gap: 8px;
    font-size: 12.5px;
    color: var(--text-gray);
  }
  .contact-icon {
    width: 16px;
    height: 16px;
    border-radius: 3px;
    background: var(--brand-red);
    display: flex;
    align-items: center;
    justify-content: center;
  }

  /* Address band */
  .address-band {
    position: absolute;
    left: 0;
    right: 0;
    top: 232px;
    height: 30px;
    background: var(--charcoal);
    color: #f2f2f2;
    font-size: 12.5px;
    display: flex;
    align-items: center;
    padding-left: 34px;
    letter-spacing: 0.2px;
  }

  /* Back */
  .card-back .lockup {
    top: 50%;
    left: 50%;
    transform: translate(-50%, -50%);
    gap: 18px;
  }
  .card-back .lockup-mark { width: 58px; height: 58px; }
  .card-back .lockup-name { font-size: 36px; letter-spacing: 0.5px; }
  .card-back .lockup-sub { font-size: 11px; letter-spacing: 9px; margin-top: 8px; }
</style>
</head>
<body>

  <section class="card card-front">
    <div class="lockup">
      <div class="lockup-mark"></div>
      <div class="lockup-divider"></div>
      <div class="lockup-text">
        <div class="lockup-name">MARLOWE</div>
        <div class="lockup-sub">Engineering</div>
      </div>
    </div>

    <div class="person">
      <div class="person-name">DANIEL R. HAYES</div>
      <div class="person-title">Managing Director</div>
    </div>

    <ul class="contacts">
      <li class="contact-item">
        <span class="contact-icon">
          <svg width="10" height="10" viewBox="0 0 10 10"><path d="M2 1 L3.8 1 L4.4 3 L3.4 3.8 Q4.3 5.7 6.2 6.6 L7 5.6 L9 6.2 L9 8 Q9 9 8 9 Q1 8.5 1 2 Q1 1 2 1 Z" fill="#fff"/></svg>
        </span>
        +00 987 654 32
      </li>
      <li class="contact-item">
        <span class="contact-icon">
          <svg width="10" height="10" viewBox="0 0 10 10"><rect x="1" y="2" width="8" height="6" fill="none" stroke="#fff" stroke-width="1.2"/><path d="M1 2 L5 5.5 L9 2" fill="none" stroke="#fff" stroke-width="1.2"/></svg>
        </span>
        office@marlowe-eng.com
      </li>
      <li class="contact-item">
        <span class="contact-icon">
          <svg width="10" height="10" viewBox="0 0 10 10"><path d="M2 1 L8 5 L5.2 5.6 L6.8 8.8 L5.6 9.3 L4 6.2 L2 8 Z" fill="#fff"/></svg>
        </span>
        www.marlowe-eng.com
      </li>
    </ul>

    <div class="address-band">2210 Canyon Ridge Drive Provo, UT 84604</div>
  </section>

  <section class="card card-back">
    <div class="lockup">
      <div class="lockup-mark"></div>
      <div class="lockup-text">
        <div class="lockup-name">MARLOWE</div>
        <div class="lockup-sub">Engineering</div>
      </div>
    </div>
  </section>

</body>
</html>
```